“Be Part Of History! Great Web Design Needed For Local Business!”

Note: This is for design only. No coding required. We want to see your ideas for a great website! This will be a FUN design and not boring like others you may work on.

WE HAVE HAD ONLY 8 DESIGNERS SO FAR SUBMIT - THIS IS A WIDE OPEN CONTEST THAT COULD MAKE YOU GOOD MONEY. PLEASE CONSIDER JOINING!

Look we are needing a great website design for a local carpet cleaning business….I know you are asking how can you “be part of history” with a boring industry like carpet cleaning. Here is the deal….NO ONE in our city has a great design so when you are chosen as the designer you are literally making history by bringing a great design to our city in this industry…

I know it’s cheesy but I am trying to get you to use your skills to help us and make it fun at the same time.

Why work with us:

We are a professional company that has run hundreds of crowdsourced projects on multiple platforms. If you participate in this contest (we hope you do) you can expect great video feedback, consistent feedback, and also our guarantee that if we know your website design will not be what we are looking for we will notify you so you don’t waste your time if there is no chance of you winning.

We respect and recognize this is how you make your living and we will not play games. We look forward to an awesome contest and awesome website designs.

Design Brief:

For this project please let your creative ideas flow. We have given you a ton of info along with videos to help you understand what we are after, however we WANT your creativity to shine through in your designs!

We are looking for a fresh and fun new design for

http://www.brightloomfloors.example/

This is a local carpet cleaning company that does great work. Unfortunately the current web design is old, outdates, and looks like dirt. So how can they portray a great image with the site they currently have? They can’t so that is why we need your help.

This website needs to convey trust, professionalism, and be super clean and easy to navigate. People making decisions for carpet cleaners are doing this fast so we need to make the site stand out and easy to navigate.

As you can see the current site does not convey trust, looks amateur and does not make people believe that this business has been in business 20 years…this is actually the top company in Albuquerque, but the current site does not reflect that…

Here is a video to help explain what we like about the current site and what we don’t like:

http://clipvault.example/t/qWm4Rt8L

Here are some examples of other sites in their business that have some things we like:

http://www.fernwaycleaners.example/ Please watch video to learn what we like and don’t like:
http://clipvault.example/t/Zp3vHsLkWaQ

http://www.tidyharbor.example/ Please watch video to learn what we like and don’t like:
http://clipvault.example/t/jRw2TbXe

http://lorenvask.example/ Please watch video to learn what we like and don’t like:
http://clipvault.example/t/NdhuwqAy

http://willowbankcarpetcleaning.example/ Please watch video to learn what we like and don’t like:
http://clipvault.example/t/GTRP4XbmZ

NOTE: We do not want to copy anything outright. We want to learn, model and take their ideas and make them better. We also want to be flexible and take what we like along with your creativity to make an amazing design.

Here is what we are looking for in more specific terms:

Colors: We need to keep the teal/turquoise look of the site. But we need some contrasting colors. Also the client likes white “its clean” so we can use white space in this.

When looking at colors please know that the current site and look is NOT what we are going for. We are going for a clean and professional look but also a look that is BOLD, FUN, and Vibrant (hence the colors).

Menu: Horizontal. We like bold and easy to read menu items. Don’t make it small and cluttered.

Site Structure: Clean and easy to navigate. We have a lot of content to display so we need a clean structure that breaks up the text and content areas.

Images: Please pull images from the current site. We can always replace the images of course, but if you show them “their own stuff” in the new design you will be closer to winning because it will feel more like “them”

Look and Feel: Professional company, trusted, and makes people feel comfortable once they are there. We need to also convey clean and crisp. That is what people are looking for from them.

Content Areas: It is a safe bet that if it is on the current site we need it on the new site. So don’t drop anything as it makes it hard to “cut content”.

What we don't want: We do not want clutter, boring, or templates or themes. We don’t want too cartoony, too cute, or too fancy… Be creative!

WIREFRAME: http://clipvault.example/t/WsLoxPea

Out of respect to professional designers who really are working hard to win if you do not follow this brief, you submit worn out themes, templates, or boring designs you will be eliminated. We are offering great prize money for this so we expect great visual designs.

We look forward to seeing your great work! Please ask any question if you have them. We will be very responsive throughout this whole contest!

Hi all, I appreciate each of you for taking the time to submit designs. I have spend a considerable amount of time today creating feedback for each of you in written and video format. We are serious about this project and are looking forward to seeing new designs. Thank you! Dale

Hi all, First I want to thank all the designers. We have many good designs and at this point are working with our client to give feedback to all of you. If we gave you feedback them please complete our requests to be considered. If you submitted a design and have not received feedback it means your design is really good, and we are sharing with our clients to get feedback so we don't waste your time on unnecessary changes. Thanks for your patience and we will get back to you soon. Dale

Reason: Hi guys, Client was on vacation and is taking a bit more time to get us feedback. Thanks, Dale

Reason: Extending to allow designers to accommodate changes for us. Dale

Target Market(s)

Most of our clients are higher end affluent. On the residential side we mostly have females calling to book appointments for our service.

We also have large businesses like apartment complexes, office buildings etc calling for our services as well.

Industry/Entity Type

Business

Font styles to use
Sans Serif

Requirements
Must have
• Space for video
Horizontal Menu
Bold
Crisp and Clean
Nice to have
• Coupons, testimonials, services,
Should not have
• cluttered
vertical menu
template look

```html
<!DOCTYPE html>
<html lang="en">
<head>
<meta charset="utf-8">
<title>Brightloom Clean — Carpet &amp; Upholstery Cleaning</title>
<link rel="stylesheet" href="https://fonts.googleapis.com/css2?family=Nunito+Sans:wght@400;600;700;800&family=Cabin:wght@400;500&display=swap">
<style>
:root{
  --teal:#0e8fae;
  --teal-text:#1590b0;
  --green:#17774d;
  --ink:#2b2b2b;
  --body:#555;
  --muted:#a5a5a5;
  --line:#dcdcdc;
  --panel:#eeeeee;
  --band:#e4e4e4;
  --footer:#5b5b5b;
  --footer-dark:#434343;
  --white:#fff;
}
*{box-sizing:border-box;margin:0;padding:0}
html,body{width:705px;height:1200px;overflow:hidden;background:var(--white)}
body{position:relative;font-family:"Nunito Sans",Arial,sans-serif;color:var(--ink)}
.abs{position:absolute}

/* header */
.brand{left:66px;top:18px;font-size:25px;font-weight:800;color:var(--teal);letter-spacing:.2px}
.brand-mark{display:inline-block;width:14px;height:14px;background:var(--green);border-radius:50%;margin-right:8px;vertical-align:1px}
.tagline{left:88px;top:50px;font-size:9px;font-weight:700;color:var(--green);letter-spacing:.4px}
.contact-top{right:66px;top:18px;font-size:8.5px;line-height:16px;text-align:right}
.contact-top svg{vertical-align:-2px;margin-right:5px}
.header-rule{left:0;top:68px;width:705px;height:1px;background:var(--line)}
.nav{left:80px;top:68px;height:27px;display:flex;gap:0;font-size:7.6px;font-weight:600;color:#444}
.nav span{line-height:27px;margin-right:28px}
.nav .active{color:var(--teal)}

/* hero */
.hero-band{left:0;top:382px;width:705px;height:68px;background:var(--band)}
.hero-photos{left:360px;top:95px;width:345px;height:287px;background:linear-gradient(135deg,#8d8c88 0%,#c8c3bc 40%,#e7e2db 60%,#b6aea4 100%)}
.hero-slant{left:0;top:95px}
.hero-title{left:65px;top:148px;font-size:19px;font-weight:400;color:var(--white);line-height:27px;letter-spacing:.3px}
.hero-title b{font-weight:800}
.hero-copy{left:65px;top:205px;width:300px;font-size:7.6px;line-height:13px;color:var(--white)}
.btn{top:243px;height:26px;font-size:11px;color:var(--white);display:flex;align-items:center;justify-content:center;border-radius:2px}
.btn-learn{left:65px;width:98px;background:var(--green)}
.btn-quote{left:180px;width:99px;border:1px solid var(--white)}
.arrow{top:217px;width:32px;height:32px;background:#0c4f61;display:flex;align-items:center;justify-content:center}
.arrow-left{left:13px}
.arrow-right{left:660px;background:#0d6f86}

/* services */
.services{left:65px;top:326px;width:575px;height:106px;background:var(--white);display:flex;border-radius:2px}
.service{flex:1;border-right:1px solid var(--line);text-align:center;padding-top:22px;font-size:9.6px;line-height:14px;color:var(--teal-text)}
.service:last-child{border-right:0}
.service svg{display:block;margin:0 auto 12px;height:32px}

/* welcome */
.welcome{left:0;top:471px;width:705px;text-align:center;font-size:13.5px}
.welcome span{color:var(--teal-text)}
.welcome-copy{left:74px;top:502px;width:557px;text-align:center;font-size:7.4px;line-height:13.5px;color:#444}

.section-head{left:65px;width:575px;text-align:center}
.section-head .rule{position:absolute;left:0;right:0;top:9px;height:1px;background:var(--line)}
.section-head .dot{position:absolute;top:5px;width:8px;height:8px;border-radius:50%;background:var(--line)}
.section-head h2{position:relative;display:inline-block;background:var(--white);padding:0 12px;font-family:"Cabin",Arial,sans-serif;font-weight:400;font-size:12.5px;color:var(--ink)}
.section-head p{font-family:"Cabin",Arial,sans-serif;font-size:6.6px;color:var(--muted);margin-top:1px}

/* portfolio */
.portfolio{left:65px;top:640px;display:flex;gap:14px}
.tile{width:133px}
.tile-photo{height:104px}
.tile-cap{height:32px;background:var(--panel);border-top:3px solid #d8d8d8;text-align:center;font-family:"Cabin",Arial,sans-serif;padding-top:3px}
.tile-cap b{display:block;font-weight:400;font-size:9.6px;color:#333}
.tile-cap small{font-size:6.8px;color:var(--muted)}

/* testimonials */
.quote{top:868px;width:284px;height:68px}
.quote-box{position:absolute;left:60px;top:6px;width:224px;height:60px;background:var(--panel);border-bottom:2px solid #d6d6d6;padding:10px 12px 0 40px;font-size:7.2px;line-height:13px;color:#555}
.quote-box .mark{position:absolute;left:22px;top:8px;font-size:16px;font-weight:800;color:#9a9a9a;line-height:14px}
.quote-box .who{position:absolute;right:12px;bottom:8px;font-size:8.6px;color:#333}
.avatar{position:absolute;left:0;top:0;width:76px;height:76px;border-radius:50%;border:5px solid #dedede}

/* footer */
.footer{left:0;top:968px;width:705px;height:196px;background:var(--footer);color:#e4e4e4}
.footer h3{position:absolute;top:16px;font-size:9.8px;font-weight:700;color:var(--white)}
.footer-links{position:absolute;left:65px;top:46px;font-size:7.6px;line-height:17.6px;color:#ddd}
.posts{position:absolute;left:176px;top:44px;width:120px}
.post{display:flex;gap:7px;height:47px;border-bottom:1px solid #777;padding-top:4px}
.post + .post{margin-top:1px;padding-top:6px}
.thumb{width:31px;height:31px;border:2px solid #888;flex:none}
.post p{font-size:7.4px;color:#e4e4e4;line-height:11px}
.post small{display:block;font-size:5.8px;color:#999;line-height:8px}
.contact-list{position:absolute;left:343px;top:50px;font-size:7.6px;line-height:12px;color:#ddd}
.contact-list div{position:relative;padding-left:20px;margin-bottom:12px}
.contact-list svg{position:absolute;left:0;top:2px}
.map{position:absolute;left:482px;top:18px;width:158px;height:129px;border:2px solid #ddd;background:linear-gradient(160deg,#efe9dc,#e4dccb 60%,#f1c48a)}
.bottom-bar{left:0;top:1164px;width:705px;height:36px;background:var(--footer-dark);color:var(--white);font-size:7.6px}
.bottom-bar .copy{position:absolute;left:65px;top:13px}
.bottom-bar .legal{position:absolute;right:65px;top:13px}
</style>
</head>
<body>

<header>
  <div class="abs brand"><span class="brand-mark"></span>Brightloom Clean</div>
  <div class="abs tagline">CARPET &amp; UPHOLSTERY CLEANING · 24 HOUR EMERGENCY SERVICE</div>
  <div class="abs contact-top">
    <div><svg width="10" height="9" viewBox="0 0 10 9"><rect x="1" y="3" width="8" height="6" rx="1" fill="#333"/><path d="M0 3 Q5 -1 10 3" stroke="#333" stroke-width="1.4" fill="none"/></svg>(505) 555-0182</div>
    <div><svg width="10" height="8" viewBox="0 0 10 8"><path d="M0 3 L5 0 L10 3 V8 H0 Z" fill="#333"/><path d="M1 3 L5 6 L9 3" stroke="#fff" stroke-width=".8" fill="none"/></svg>info@brightloomfloors.example</div>
  </div>
  <div class="abs header-rule"></div>
  <nav class="abs nav">
    <span class="active">HOME</span><span>ABOUT</span><span>SERVICES</span><span>BLOG</span><span>EQUIPMENT RENTALS</span><span>TESTIMONIALS</span><span>FREE VIDEOS</span><span>CONTACT US</span>
  </nav>
</header>

<section class="hero">
  <div class="abs hero-band"></div>
  <div class="abs hero-photos" role="img" aria-label="Collage of clean living rooms, tiled floors and dining spaces"></div>
  <svg class="abs hero-slant" width="410" height="287" viewBox="0 0 410 287"><path d="M0 0 H362 L408 231 H410 V287 H0 Z" fill="var(--teal)"/></svg>
  <h1 class="abs hero-title">We Provide You With The <b>BEST</b><br>Cleaning <b>EXPERIENCE</b></h1>
  <p class="abs hero-copy">Lorem Ipsum is simply dummy text of the printing and typesetting industry. Lorem Ipsum has been the industry's</p>
  <div class="abs btn btn-learn">Learn More</div>
  <div class="abs btn btn-quote">Get a Qoute</div>
  <div class="abs arrow arrow-left"><svg width="10" height="10" viewBox="0 0 10 10"><path d="M7 1 L3 5 L7 9" stroke="#fff" stroke-width="2" fill="none"/></svg></div>
  <div class="abs arrow arrow-right"><svg width="10" height="10" viewBox="0 0 10 10"><path d="M3 1 L7 5 L3 9" stroke="#fff" stroke-width="2" fill="none"/></svg></div>

  <div class="abs services">
    <div class="service">
      <svg width="20" height="32" viewBox="0 0 20 32"><rect x="2" y="3" width="16" height="26" fill="#333"/><path d="M10 9 L15 16 L10 23 L5 16 Z" fill="#fff"/><path d="M3 1 V3 M6 1 V3 M9 1 V3 M12 1 V3 M15 1 V3 M3 29 V31 M6 29 V31 M9 29 V31 M12 29 V31 M15 29 V31" stroke="#333"/></svg>
      Carpet and Upholstery<br>Cleaning
    </div>
    <div class="service">
      <svg width="32" height="32" viewBox="0 0 32 32"><g transform="rotate(-45 16 16)"><rect x="2" y="11" width="28" height="10" rx="1" fill="none" stroke="#333" stroke-width="1.5"/><path d="M8 11 V21 M14 11 V21 M20 11 V21 M26 11 V21" stroke="#333"/></g></svg>
      Tile and Grout<br>Cleaning
    </div>
    <div class="service">
      <svg width="32" height="32" viewBox="0 0 32 32"><g fill="none" stroke="#333" stroke-width="1.8"><rect x="2" y="2" width="12" height="12"/><rect x="18" y="2" width="12" height="12"/><rect x="2" y="18" width="12" height="12"/><rect x="18" y="18" width="12" height="12"/></g></svg>
      Strip and Wax<br>Floors
    </div>
    <div class="service">
      <svg width="40" height="32" viewBox="0 0 40 32"><path d="M2 9 H24 V12 H32 L38 19 V26 H2 Z" fill="#333"/><circle cx="10" cy="26" r="4" fill="#333" stroke="#fff" stroke-width="1.5"/><circle cx="31" cy="26" r="4" fill="#333" stroke="#fff" stroke-width="1.5"/><path d="M26 14 H31 L35 19 H26 Z" fill="#fff"/></svg>
      RVs and Cars
    </div>
  </div>
</section>

<section>
  <h2 class="abs welcome">Welcome to <span>Brightloom Clean</span></h2>
  <p class="abs welcome-copy">Lorem ipsum dolor sit amet, consectetuer adipiscing elit, sed diam nonummy nibh euismod tincidunt ut laoreet dolore magna aliquam erat volutpat. Ut wisi enim ad minim veniam, quis nostrud exerci tation ullamcorper suscipit lobortis nisl ut aliquip ex ea commodo consequat.Lorem ipsum dolor sit amet, consectetuer adipiscing elit, sed diam nonummy nibh euismod tincidunt ut laoreet dolore magna aliquam erat volutpat. Ut wisi enim ad minim veniam, quis nostrud exerci tation ullamcorper suscipit lobortis nisl ut aliquip ex ea commodo consequat.</p>
</section>

<section>
  <div class="abs section-head" style="top:578px">
    <div class="rule"></div><div class="dot" style="left:228px"></div><div class="dot" style="left:343px"></div>
    <h2>Our Portfolio</h2><p>Lorem Ipsum Dolor Sit Amet</p>
  </div>
  <div class="abs portfolio">
    <div class="tile"><div class="tile-photo" role="img" aria-label="Bedroom with fresh beige carpet" style="background:linear-gradient(#dcd6cc,#9b8e7e)"></div><div class="tile-cap"><b>Carpeting</b><small>Lorem Ipsum Dolor</small></div></div>
    <div class="tile"><div class="tile-photo" role="img" aria-label="Light tiled floor with red chair" style="background:linear-gradient(135deg,#e4e2df,#d9d5d0 60%,#c4553a)"></div><div class="tile-cap"><b>Tiles</b><small>Lorem Ipsum Dolor</small></div></div>
    <div class="tile"><div class="tile-photo" role="img" aria-label="Polished timber floor with sofa" style="background:linear-gradient(#5a5450 0%,#8c8580 35%,#e3c08b 60%,#d6a868)"></div><div class="tile-cap"><b>Timber</b><small>Lorem Ipsum Dolor</small></div></div>
    <div class="tile"><div class="tile-photo" role="img" aria-label="White vinyl floor with wire chairs" style="background:linear-gradient(#2fa3a8 0%,#e6e6e4 25%,#efefed)"></div><div class="tile-cap"><b>Vinyl</b><small>Lorem Ipsum Dolor</small></div></div>
  </div>
</section>

<section>
  <div class="abs section-head" style="top:812px">
    <div class="rule"></div><div class="dot" style="left:220px"></div><div class="dot" style="left:350px"></div>
    <h2>Client Testimonials</h2><p>Lorem Ipsum Dolor Sit Amet</p>
  </div>
  <div class="abs quote" style="left:65px">
    <div class="quote-box"><span class="mark">“</span>Nunc at pretium est curabitur commodo leac est venenatis egestas sed aliquet auguevelit<span class="who">Lorem Ipsum</span></div>
    <div class="avatar" role="img" aria-label="Portrait of a male client" style="background:radial-gradient(#c9a58d,#6e5a4f)"></div>
  </div>
  <div class="abs quote" style="left:363px">
    <div class="quote-box"><span class="mark">“</span>Nunc at pretium est curabitur commodo leac est venenatis egestas sed aliquet auguevelit<span class="who">Lorem Ipsum</span></div>
    <div class="avatar" role="img" aria-label="Portrait of a female client" style="background:radial-gradient(#d4ab90,#5a3d30)"></div>
  </div>
</section>

<footer>
  <div class="abs footer">
    <h3 style="left:65px">Brightloom Cities</h3>
    <div class="footer-links">Lorem ipsum<br>Dolor sit<br>Amet consec<br>Adipicsing<br>Diam set<br>Nonummy</div>

    <h3 style="left:176px">Latest Blog Posts</h3>
    <div class="posts">
      <div class="post"><div class="thumb" role="img" aria-label="Pink flower" style="background:#a67aa8"></div><p>Lorem ipsum Dolor sit<small>December 05,2014<br>50 Comments</small></p></div>
      <div class="post"><div class="thumb" role="img" aria-label="White daisy" style="background:#4f7a3a"></div><p>Amet consec Adipicsing<small>December 05,2014<br>50 Comments</small></p></div>
      <div class="post"><div class="thumb" role="img" aria-label="Orange butterfly" style="background:#c07a2e"></div><p>Diam set Nonummy<small>December 05,2014<br>50 Comments</small></p></div>
    </div>

    <h3 style="left:343px">Contact Us</h3>
    <div class="contact-list">
      <div><svg width="10" height="9" viewBox="0 0 10 9"><path d="M5 0 L10 4.5 H8.5 V9 H6 V6 H4 V9 H1.5 V4.5 H0 Z" fill="#fff"/></svg>2740 Larkspur Blvd.<br>Albuquerque, NM, 87110<br>United States</div>
      <div><svg width="10" height="9" viewBox="0 0 10 9"><rect x="1" y="3" width="8" height="6" rx="1" fill="#fff"/><path d="M0 3 Q5 -1 10 3" stroke="#fff" stroke-width="1.4" fill="none"/></svg>(505) 555-0182</div>
      <div><svg width="10" height="8" viewBox="0 0 10 8"><rect x="0" y="1" width="10" height="7" fill="#fff"/><path d="M0 1 L5 5 L10 1" stroke="#5b5b5b" fill="none"/></svg>info@brightloomfloors.example</div>
    </div>

    <div class="map" role="img" aria-label="Street map showing the company location in Albuquerque"></div>
  </div>
  <div class="abs bottom-bar">
    <span class="copy">Copyright © Brightloom Clean, LLC, 2011. All rights reserved.</span>
    <span class="legal">Privacy Policy &nbsp;|&nbsp; Terms &amp; Contitions</span>
  </div>
</footer>

</body>
</html>
```